Cyber Security Site Design (Products & Consulting)

I need my website redesigned to be engaging, clean, efficient and modern. My company (when its up and running) is going to be concentrated on two things: a few specific products for cyber security as well as cyber security consulting services. The background I bring to the field is having worked with small companies all the way to the largest government organizations and advising them on their security posture and how to improve it. We need the ability to add products and services easily.

For a sample product, you can use either Tarnel (http://www.tarnel-relay.org/) or Vornidex Graywell (https://www.vornidex.com/products/relay-kx-and-enhanced-safe-portal).

It will replace https://dalmorenvue.com/

Target Market(s)

Cyber Security professionals in all verticals

Coding

Coded - Design and coding required

Number of Pages Required

4 page

Font styles to use
Sans Serif

Colors
6b449b

Requirements
Must have
• Ability to easily modify
• Have main page
• Have product specific pages
• Have consulting services pages
• Have executive team information
• Clean, modern design
• Usage of the logo and its color scheme
Nice to have
• I like the idea of a left collapsed sidebar (so icons only) that can expand for text.
• I am also open to a very unique landing page, possibly a shape in the middle (hexagons maybe?) with each of the options there.
Should not have
• Nothing that looks like it came out of a hacker movie

```html
<!DOCTYPE html>
<html lang="en">
<head>
<meta charset="UTF-8">
<title>Dalmoren – Cyber Security</title>
<link href="https://fonts.googleapis.com/css2?family=Raleway:wght@400;500;600;700&family=Mulish:wght@400;600&display=swap" rel="stylesheet">
<style>
  :root {
    --bg: #2a173f;
    --bg-stripe: #2e1a45;
    --bar: #1d0f2e;
    --hex-face: #301b48;
    --hex-edge: #3a2356;
    --brand: #6b449b;
    --brand-light: #8a63bd;
    --white: #ffffff;
    --muted: #8e7ea8;
    --line: #8b7aa6;
    --accent: #39c6e6;
  }
  * { margin: 0; padding: 0; box-sizing: border-box; }
  html, body { width: 1200px; height: 3248px; overflow: hidden; }
  body {
    background: var(--bg);
    font-family: "Raleway", sans-serif;
    color: var(--white);
  }
  .page {
    position: relative;
    width: 1200px;
    height: 3248px;
    background: repeating-linear-gradient(90deg, var(--bg) 0 22px, var(--bg-stripe) 22px 24px);
    overflow: hidden;
  }
  .abs { position: absolute; }

  /* sidebars */
  .sidebar-left { left: 0; top: 0; width: 56px; height: 100%; background: var(--bar); }
  .sidebar-right { right: 0; top: 0; width: 60px; height: 100%; background: var(--bar); }
  .nav-icons { position: absolute; top: 140px; left: 18px; display: flex; flex-direction: column; gap: 18px; }
  .nav-icons svg { width: 20px; height: 20px; fill: var(--white); }
  .vertical-label {
    position: absolute;
    writing-mode: vertical-rl;
    transform: rotate(180deg);
    font-size: 14px; font-weight: 600;
  }
  .sidebar-left .vertical-label { left: 10px; top: 330px; }
  .sidebar-left .vertical-note { left: 32px; top: 330px; font-size: 10px; font-weight: 400; color: var(--muted); font-family: "Mulish", sans-serif; }
  .sidebar-right .vertical-label { right: 22px; top: 320px; transform: none; }
  .dots { position: absolute; right: 26px; top: 510px; display: flex; flex-direction: column; gap: 14px; }
  .dots span { width: 6px; height: 6px; border-radius: 50%; background: var(--muted); }

  /* brand */
  .brand { display: flex; align-items: center; gap: 10px; }
  .brand-mark { width: 34px; height: 34px; border-radius: 50%; background: var(--brand-light); }
  .brand-name { font-size: 30px; font-weight: 600; letter-spacing: 2px; color: var(--brand-light); }

  /* hexagons */
  .hex-pointy { clip-path: polygon(50% 0, 100% 25%, 100% 75%, 50% 100%, 0 75%, 0 25%); }
  .hex-flat { clip-path: polygon(25% 0, 75% 0, 100% 50%, 75% 100%, 25% 100%, 0 50%); }
  .hex-panel { background: linear-gradient(160deg, var(--hex-edge), var(--hex-face) 55%, #28163c); }
  .hex-shadow { filter: drop-shadow(0 10px 18px rgba(0,0,0,.45)); }

  .cell {
    position: absolute; width: 104px; height: 116px;
    background: var(--brand);
    display: flex; align-items: center; justify-content: center; text-align: center;
    font-size: 11px; line-height: 1.3; padding: 0 12px;
  }

  .hero-title { left: 82px; top: 370px; font-size: 62px; font-weight: 500; line-height: 1.1; }
  .hero-caret { left: 592px; top: 536px; width: 0; height: 0; border-left: 7px solid transparent; border-right: 7px solid transparent; border-top: 8px solid var(--muted); }

  .about-title { width: 100%; text-align: center; top: 720px; font-size: 60px; font-weight: 500; }
  .about-text {
    left: 400px; top: 810px; width: 400px; text-align: center;
    font-family: "Mulish", sans-serif; font-size: 14px; line-height: 1.55; color: #e4dcef;
  }

  /* divider ornament placeholder */
  .divider {
    left: 300px; width: 600px; height: 190px;
    background: radial-gradient(ellipse at 50% 40%, rgba(139,122,166,.22), rgba(139,122,166,.06) 60%, transparent 75%);
  }

  .media { background: linear-gradient(135deg, #2d5f86, #1b2b52 60%, #3a2a6a); }
  .media-products { background: linear-gradient(135deg, #1f3a6a, #5f6fb0 55%, #2a2b5c); }
  .media-team { background: linear-gradient(135deg, #7d4fc4, #3b1f6a 60%, #1e1236); }

  .section-title { font-size: 46px; font-weight: 500; white-space: nowrap; }
  .section-text {
    font-family: "Mulish", sans-serif; font-size: 13px; line-height: 1.6; color: var(--muted); width: 430px;
  }
  .more { font-family: "Mulish", sans-serif; font-size: 12px; color: var(--muted); letter-spacing: 1px; }
  .right { text-align: right; }

  .talk-title { width: 100%; text-align: center; top: 2915px; font-size: 66px; font-weight: 600; }
  .talk-title a { color: var(--accent); text-decoration: underline; text-underline-offset: 8px; }
</style>
</head>
<body>
<div class="page">

  <aside class="abs sidebar-left">
    <nav class="nav-icons">
      <svg viewBox="0 0 20 20"><path d="M10 2 1 10h3v8h5v-5h2v5h5v-8h3z"/></svg>
      <svg viewBox="0 0 20 20"><rect x="2" y="11" width="4" height="7"/><rect x="8" y="6" width="4" height="12"/><rect x="14" y="2" width="4" height="16"/></svg>
      <svg viewBox="0 0 20 20"><path d="M2 3h16v11H7l-4 4v-4H2z"/></svg>
      <svg viewBox="0 0 20 20"><circle cx="10" cy="6" r="4"/><path d="M2 19c0-5 4-7 8-7s8 2 8 7z"/></svg>
    </nav>
    <div class="vertical-label">About Us</div>
    <div class="vertical-label vertical-note">Security posture advice</div>
  </aside>

  <aside class="abs sidebar-right">
    <div class="vertical-label">Contact Us</div>
    <div class="dots"><span></span><span></span><span></span></div>
  </aside>

  <div class="abs brand" style="left:100px; top:34px;">
    <span class="brand-mark"></span>
    <span class="brand-name">DALMOREN</span>
  </div>

  <!-- hero -->
  <div class="abs hex-shadow" style="left:350px; top:20px; width:510px; height:520px;">
    <div class="hex-pointy hex-panel" style="width:100%; height:100%;"></div>
  </div>
  <div class="abs" style="left:0; top:0; width:1200px; height:560px;">
    <div class="cell hex-pointy" style="left:624px; top:84px;">Identity Management</div>
    <div class="cell hex-pointy" style="left:478px; top:136px;">Endpoint Security</div>
    <div class="cell hex-pointy" style="left:374px; top:196px;">Network Security</div>
    <div class="cell hex-pointy" style="left:478px; top:256px;">Data Security</div>
    <div class="cell hex-pointy" style="left:586px; top:196px;">Mobile Security</div>
    <div class="cell hex-pointy" style="left:692px; top:256px;">End - User Education</div>
    <div class="cell hex-pointy" style="left:374px; top:314px;">Application Security</div>
    <div class="cell hex-pointy" style="left:586px; top:314px;">Cloud Security</div>
    <div class="cell hex-pointy" style="left:692px; top:374px;">Database Security</div>
  </div>
  <h1 class="abs hero-title">Cyber<br>Security</h1>
  <div class="abs hero-caret"></div>

  <!-- about -->
  <div class="abs hex-shadow" style="left:340px; top:600px; width:520px; height:600px;">
    <div class="hex-pointy hex-panel" style="width:100%; height:100%;"></div>
  </div>
  <h2 class="abs about-title">About Us</h2>
  <p class="abs about-text">We help teams of every size see their security posture clearly and improve it. From small firms to large public bodies, we review systems, test defences and build practical plans. Our products and advisory work share one goal: calm, steady protection that people can actually use every day.</p>

  <div class="abs divider" role="img" aria-label="Decorative divider ornament between sections" style="top:1170px;"></div>

  <!-- security consulting -->
  <div class="abs hex-flat media" role="img" aria-label="Abstract digital security visual in teal and navy" style="left:180px; top:1400px; width:310px; height:220px;"></div>
  <h3 class="abs section-title" style="left:180px; top:1622px;">Security Consulting</h3>
  <p class="abs section-text" style="left:180px; top:1700px;">Clear reviews of your security posture, with practical steps to close gaps. We work with small companies and large agencies alike, and leave your team stronger.</p>
  <span class="abs more" style="left:180px; top:1782px;">more &rarr;</span>

  <!-- security products -->
  <div class="abs hex-flat media-products" role="img" aria-label="Data visualisation graphic in blue tones" style="left:720px; top:1640px; width:300px; height:220px;"></div>
  <h3 class="abs section-title right" style="right:180px; top:1880px;">Security Products</h3>
  <p class="abs section-text right" style="right:180px; top:1956px;">Focused tools such as Tarnel and Vornidex Graywell, configured and supported by our team to filter traffic and guard the edge of your network.</p>
  <span class="abs more" style="right:180px; top:2030px;">more &rarr;</span>

  <!-- executive team -->
  <div class="abs hex-flat media-team" role="img" aria-label="Silhouettes of the executive team against a violet glow" style="left:180px; top:1890px; width:310px; height:230px;"></div>
  <h3 class="abs section-title" style="left:180px; top:2140px;">Executive Team</h3>
  <p class="abs section-text" style="left:180px; top:2216px;">Decades of advisory work across private firms and government bodies. Meet the people who will guide your security programme from first review onward.</p>
  <span class="abs more" style="left:180px; top:2300px;">more &rarr;</span>

  <div class="abs divider" role="img" aria-label="Decorative divider ornament between sections" style="top:2420px;"></div>

  <!-- let's talk -->
  <div class="abs hex-shadow" style="left:290px; top:2620px; width:620px; height:560px;">
    <div class="hex-flat hex-panel" style="width:100%; height:100%;"></div>
  </div>
  <div class="abs brand" style="left:480px; top:2840px;">
    <span class="brand-mark"></span>
    <span class="brand-name">DALMOREN</span>
  </div>
  <h2 class="abs talk-title">Let's <a href="#contact">talk</a></h2>

</div>
</body>
</html>
```